Pivots & Treads .com

This website is simple!!!
Landing page background image should capture the customers attention!!! We will provide a image as a example of what we like. The purpose for this website is to provide customers with a clean easy way to request a quote for industrial casters and wheels by OEM’s as well as maintenance departments worldwide. Please see if you can follow our thought process below.
Customer comes to website, they are invited to Request a Quote by providing us with Manufacturer Name, Manufacturers Part # and quantity needed.
If this is not known the customer will complete will WP conversation format form answering about 10 questions
Or
Look up the part number in one of the 8 to 12 catalogs located in the PageTurn Book format on our catalog page, or equal plug in .
When the client request a quote a account page will pop up request The following:
Clients first and last name
Email address
And optional questions
Company name and best contact number.
Once this is complete customer will hit SUBMIT.
The customers request will be in system. A email will be sent to Customer service notifying us the Quote Request has been made.
We will then build a quote for the customer with a good, better and best options. Customers Request a Quote submission may have more than one caster or wheel requested at a time, so website must allow this.
When the customer comes back into website there email address will come up as the account name and request a password be made for them. This will allow them to store quotes in their account for future needs. If quote is older than 30 day the system will trigger a button at the bottom of the quote for resubmit Request for updated quote.
Once customer reviews quote the quote can be Converted to order within the website.
Once Converted the system will send us a email and order will be processed.
We will need a Chat program that will text to CS the questions.
You will need to have high quality graphic design skills on your team.
We have found 2 plugins that would work nicely with our new website Flippin books to showcase our catalogs for customers to research and WPForms conversation forms to complete request for quote form.
Just Ideas:
Very very ghosted caster blueprint in white background but very very ghosted or the icon just idea
We have never had a font used we like
Grayscale every except for rubber on wheels and logo icon
Website should have hamburger menu on left
Website should hav responsive deign
Account head on right side
Has anyone read the brief from top to bottom and the updates, I’m seeing a lot of duplicates of the website I posted in images I want a clean website With lite backgrand with the poly being definite colors on each wheel I added a green yellow and red image has anyone looked at that Just a question?
Went on vacation/holiday

```html
<!DOCTYPE html>
<html lang="en">
<head>
<meta charset="utf-8">
<title>Pivots &amp; Treads .com</title>
<link href="https://fonts.googleapis.com/css2?family=Montserrat:wght@400;500;600;700&display=swap" rel="stylesheet">
<style>
  :root {
    --hero-top: #5d93f2;
    --hero-bottom: #5b4bee;
    --white: #ffffff;
    --navy: #263f8e;
    --text-grey: #6b7078;
    --section-grey: #eceef0;
    --footer-blue: #5179ef;
    --footer-dark: #3a52ad;
    --button-blue: #1f9cf4;
    --link-blue: #3f7cf0;
    --input-text: #8a8f98;
  }
  * { box-sizing: border-box; margin: 0; padding: 0; }
  html, body { width: 1134px; height: 1200px; overflow: hidden; }
  body { font-family: "Montserrat", sans-serif; background: var(--white); position: relative; }

  .hero {
    position: absolute; left: 0; top: 0; width: 1134px; height: 496px;
    background: linear-gradient(160deg, var(--hero-top) 0%, #5f82f1 45%, var(--hero-bottom) 100%);
    color: var(--white);
    overflow: hidden;
  }
  .hero-shape {
    position: absolute; border-radius: 40px; background: rgba(255,255,255,0.06);
    transform: rotate(45deg);
  }
  .brand {
    position: absolute; left: 213px; top: 28px;
    font-size: 19px; font-weight: 700; letter-spacing: -0.2px; color: var(--white);
  }
  .main-nav { position: absolute; top: 36px; left: 535px; display: flex; gap: 32px; }
  .main-nav a { color: var(--white); text-decoration: none; font-size: 8.5px; font-weight: 600; letter-spacing: 0.3px; padding-bottom: 2px; }
  .main-nav a.active { border-bottom: 1px solid var(--white); }
  .account-icon { position: absolute; left: 840px; top: 29px; }
  .login-btn {
    position: absolute; left: 876px; top: 28px; width: 46px; height: 24px;
    border: 1px solid var(--white); border-radius: 2px;
    font-size: 8.5px; font-weight: 600; display: flex; align-items: center; justify-content: center;
  }
  .headline { position: absolute; left: 210px; top: 134px; font-size: 32px; font-weight: 700; letter-spacing: -0.5px; }
  .steps { position: absolute; left: 213px; top: 186px; list-style: none; }
  .steps li { font-size: 12.5px; line-height: 18.5px; display: flex; gap: 11px; }
  .steps b { font-weight: 700; width: 6px; }
  .quote-form { position: absolute; left: 213px; top: 252px; width: 208px; }
  .quote-field {
    display: block; width: 208px; height: 25px; margin-bottom: 12px;
    background: var(--white); border-radius: 2px; border: none;
    font-family: inherit; font-size: 9px; color: var(--input-text); padding-left: 10px; line-height: 25px;
  }
  .form-actions { display: flex; gap: 8px; margin-top: 1px; }
  .btn { height: 32px; border-radius: 3px; font-size: 9px; font-weight: 600; letter-spacing: 0.3px; display: flex; align-items: center; justify-content: center; }
  .btn-quote { width: 105px; background: var(--white); color: var(--link-blue); }
  .btn-catalog { width: 95px; background: var(--button-blue); color: var(--white); }
  .hero-note { position: absolute; left: 213px; top: 419px; font-size: 9px; line-height: 10px; width: 320px; }
  .product-visual {
    position: absolute; left: 500px; top: 160px; width: 380px; height: 240px; border-radius: 30px;
    background: radial-gradient(ellipse at 65% 55%, rgba(40,55,110,0.55), rgba(90,110,180,0.25) 55%, rgba(255,255,255,0) 75%);
  }

  .goal { position: absolute; left: 0; top: 496px; width: 1134px; height: 143px; background: var(--white); }
  .section-title { color: var(--navy); font-weight: 500; text-align: center; }
  .goal .section-title { position: absolute; top: 24px; width: 100%; font-size: 23px; }
  .body-copy { position: absolute; font-size: 8px; line-height: 7.8px; color: var(--text-grey); }
  .goal .body-copy { left: 344px; top: 69px; width: 472px; }

  .worldwide { position: absolute; left: 0; top: 639px; width: 1134px; height: 424px; background: var(--section-grey); }
  .worldwide .section-title { position: absolute; top: 26px; width: 100%; font-size: 24px; }
  .world-map {
    position: absolute; left: 212px; top: 81px; width: 694px; height: 286px; border-radius: 60px;
    background: radial-gradient(ellipse at center, #c9cfd6 0%, #dde1e5 55%, var(--section-grey) 80%);
  }
  .worldwide .body-copy { left: 462px; top: 353px; width: 324px; }

  .site-footer { position: absolute; left: 0; top: 1063px; width: 1134px; height: 114px; background: var(--footer-blue); color: var(--white); font-size: 8.5px; }
  .footer-col { position: absolute; top: 24px; list-style: none; }
  .footer-col li { line-height: 17px; }
  .address { left: 240px; }
  .links-a { left: 583px; }
  .links-b { left: 678px; }
  .footer-bar { position: absolute; left: 0; top: 1177px; width: 1134px; height: 23px; background: var(--footer-dark); color: var(--white); font-size: 9.5px; font-weight: 600; text-align: center; line-height: 23px; }
</style>
</head>
<body>
  <header class="hero">
    <div class="hero-shape" style="left:60px;top:120px;width:300px;height:300px;"></div>
    <div class="hero-shape" style="left:860px;top:70px;width:260px;height:260px;"></div>
    <div class="hero-shape" style="left:420px;top:-140px;width:280px;height:280px;"></div>

    <div class="brand">Pivots &amp; Treads .com</div>
    <nav class="main-nav">
      <a href="#" class="active">ABOUT AS</a>
      <a href="#">OUR CATALOG</a>
      <a href="#">CONTACTS</a>
    </nav>
    <svg class="account-icon" width="22" height="22" viewBox="0 0 22 22" fill="none" stroke="#fff" stroke-width="1">
      <circle cx="11" cy="11" r="10"/>
      <circle cx="11" cy="8.5" r="3.5"/>
      <path d="M4.5 18c1.5-3 3.8-4.3 6.5-4.3s5 1.3 6.5 4.3"/>
    </svg>
    <div class="login-btn">LOGIN</div>

    <h1 class="headline">Easy as 1-2-3</h1>
    <ol class="steps">
      <li><b>1</b>Request a Quote</li>
      <li><b>2</b>Receive a Quote</li>
      <li><b>3</b>Convert to Quote order</li>
    </ol>

    <form class="quote-form">
      <div class="quote-field">Manufacturer Name</div>
      <div class="quote-field">Manufacturers Part #</div>
      <div class="quote-field">Quantity</div>
      <div class="form-actions">
        <div class="btn btn-quote">REQUEST A QUOTE</div>
        <div class="btn btn-catalog">GO TO CATALOG</div>
      </div>
    </form>

    <p class="hero-note">Look up the part number in one of the 8 to 12 catalogs located in the PageTurn Book format on our catalog page, or equal plug in</p>

    <div class="product-visual" role="img" aria-label="Product photo of two industrial wheels and a swivel caster with dark blue treads"></div>
  </header>

  <section class="goal">
    <h2 class="section-title">Our Goal</h2>
    <p class="body-copy">It is a long established fact that a reader will be distracted by the readable content of a page when looking at its layout. The point of using Lorem Ipsum is that it has a more-or-less normal distribution of letters, as opposed to using 'Content here, content here', making it look like readable English. Many desktop publishing packages and web page editors now use Lorem Ipsum as their default model text, and a search for 'lorem ipsum' will uncover many web sites still in their infancy. Various versions have evolved over the years, sometimes by accident, sometimes on purpose (injected humour and the like).</p>
  </section>

  <section class="worldwide">
    <h2 class="section-title">Maintenance Departments Worldwide</h2>
    <div class="world-map" role="img" aria-label="Dotted world map with blue location pins marking maintenance departments worldwide"></div>
    <p class="body-copy">It is a long established fact that a reader will be distracted by the readable content of a page when looking at its layout. The point of using Lorem Ipsum is that it has a more-or-less normal distribution of letters, as opposed to using 'Content here, content here', making it look like readable English. Many desktop publishing packages and web page editors now use Lorem Ipsum as</p>
  </section>

  <footer class="site-footer">
    <ul class="footer-col address">
      <li>1420 LARKFIELD RD,</li>
      <li>EASTPORT FALLS,</li>
      <li>NY 14000, US</li>
    </ul>
    <ul class="footer-col links-a">
      <li>ABOUT AS</li>
      <li>OUR CATALOG</li>
      <li>CONTACTS</li>
    </ul>
    <ul class="footer-col links-b">
      <li>OUR GOALS</li>
      <li>MAINTRANCE</li>
      <li>CONTACTS</li>
    </ul>
  </footer>
  <div class="footer-bar">www.pivotsandtreads.com</div>
</body>
</html>
```